Business Card design needs editing

We have a business card design but I need to remove one of the providers. The provider to be removed is "Marlene Odgrave, Midwife.

Industry/Entity Type

Business

Contact Information for Business Card

I have uploaded a copy of our current business card

```html
<!DOCTYPE html>
<html lang="en">
<head>
<meta charset="utf-8">
<title>Willow Women's Health – Business Card</title>
<link href="https://fonts.googleapis.com/css2?family=Lato:wght@400;700&display=swap" rel="stylesheet">
<style>
  :root {
    --backdrop: #262626;
    --card: #ffffff;
    --sky: #a9cbdc;
    --sky-light: #b9d9e6;
    --stone: #928c8a;
    --ink: #7b7b7b;
    --ink-dark: #6a6a6a;
    --brand-blue: #7fbfd6;
  }
  * { margin: 0; padding: 0; box-sizing: border-box; }
  html, body { width: 1200px; height: 900px; overflow: hidden; }
  body {
    background: var(--backdrop);
    font-family: "Lato", Arial, sans-serif;
    position: relative;
  }
  .card {
    position: absolute;
    left: 260px;
    width: 680px;
    height: 388px;
    background: var(--card);
    overflow: hidden;
  }
  .card--front { top: 40px; }
  .card--back { top: 472px; }
  .card__waves { position: absolute; inset: 0; width: 100%; height: 100%; }

  .brand {
    position: absolute;
    display: flex;
    align-items: center;
    gap: 10px;
    color: var(--ink);
    font-weight: 700;
  }
  .brand__dot {
    width: 30px; height: 30px; border-radius: 50%;
    background: var(--brand-blue);
    flex: none;
  }
  .card--front .brand { left: 38px; top: 44px; font-size: 24px; }
  .brand__tagline {
    position: absolute; left: 78px; top: 78px;
    font-size: 12px; color: var(--ink); font-weight: 400;
  }

  .providers {
    position: absolute; left: 40px; top: 262px;
    list-style: none;
    color: var(--ink);
    font-weight: 700;
    font-size: 20px;
    line-height: 25px;
  }
  .contact {
    position: absolute; right: 36px; top: 185px;
    list-style: none;
    color: var(--ink);
    font-weight: 700;
    font-size: 15px;
    line-height: 23px;
    text-align: right;
  }
  .contact li { display: flex; justify-content: flex-end; align-items: center; gap: 6px; }
  .contact svg { width: 12px; height: 12px; fill: var(--ink); flex: none; }
  .contact .no-icon { padding-right: 18px; }

  .card--back .brand {
    left: 0; right: 0; top: 140px;
    justify-content: center;
    font-size: 30px;
  }
  .card--back .brand__dot { width: 40px; height: 40px; }
  .back__url {
    position: absolute; left: 0; right: 0; top: 236px;
    text-align: center;
    font-size: 18px;
    letter-spacing: 1px;
    color: var(--ink-dark);
  }
</style>
</head>
<body>

  <section class="card card--front" aria-label="Business card front">
    <svg class="card__waves" viewBox="0 0 680 388" preserveAspectRatio="none" aria-hidden="true">
      <path d="M0,182 C170,232 430,215 680,92 L680,388 L0,388 Z" fill="var(--sky)"/>
      <path d="M70,162 C260,195 470,160 680,72 L680,80 C470,172 260,205 70,162 Z" fill="var(--sky-light)"/>
      <path d="M0,160 C140,190 300,200 420,184 C300,212 140,220 0,200 Z" fill="var(--stone)"/>
    </svg>

    <div class="brand"><span class="brand__dot"></span><span>Willow Women's Health</span></div>
    <p class="brand__tagline">Obstetrics &amp; Gynecology</p>

    <ul class="providers">
      <li>Jennifer Stuckey, MD</li>
      <li>Dana Whitfield, MD</li>
      <li>Laura Benning, MD</li>
    </ul>

    <ul class="contact">
      <li>555-214-3870
        <svg viewBox="0 0 24 24"><path d="M6.6 10.8a15 15 0 0 0 6.6 6.6l2.2-2.2a1 1 0 0 1 1-.25 11.4 11.4 0 0 0 3.6.57 1 1 0 0 1 1 1V20a1 1 0 0 1-1 1A17 17 0 0 1 3 4a1 1 0 0 1 1-1h3.5a1 1 0 0 1 1 1c0 1.250.2 2.450.57 3.57a1 1 0 0 1-.25 1z"/></svg>
      </li>
      <li>555-214-3871
        <svg viewBox="0 0 24 24"><path d="M6 2h12v6H6zM4 9h16a2 2 0 0 1 2 2v6h-4v5H6v-5H2v-6a2 2 0 0 1 2-2zm4 8v3h8v-3z"/></svg>
      </li>
      <li>www.willowwomenshealth.com
        <svg viewBox="0 0 24 24"><path d="M12 2a10 10 0 1 0 0 20 10 10 0 0 0 0-20zm0 2c.8 1.2 1.5 2.5 1.9 4h-3.8c.4-1.5 1.1-2.8 1.9-4zM4.3 14a8 8 0 0 1 0-4h3.4a16 16 0 0 0 0 4zm15.4 0h-3.4a16 16 0 0 0 0-4h3.4a8 8 0 0 1 0 4zM12 20c-.8-1.2-1.5-2.5-1.9-4h3.8c-.4 1.5-1.1 2.8-1.9 4zm2.3-6H9.7a14 14 0 0 1 0-4h4.6a14 14 0 0 1 0 4z"/></svg>
      </li>
      <li>418 Linden Ave, Ste 3B
        <svg viewBox="0 0 24 24"><path d="M12 2a7 7 0 0 0-7 7c0 5 7 13 7 13s7-8 7-13a7 7 0 0 0-7-7zm0 9.5A2.5 2.5 0 1 1 12 6.5a2.5 2.5 0 0 1 0 5z"/></svg>
      </li>
      <li class="no-icon">Fairview, GA 30000-1234</li>
    </ul>
  </section>

  <section class="card card--back" aria-label="Business card back">
    <div class="brand"><span class="brand__dot"></span><span>Willow Women's Health</span></div>
    <p class="back__url">www.willowwomenshealth.com</p>
  </section>

</body>
</html>
```